International Patent Law Firm Needs a New Website Design

We are an international, German-based patent law firm and are in need for a new website design.

Our current (old-fashioned) website is

www.lwpt.example

Our Corporate Identity features that we want to keep are as follows.

1. Our LWPT logo in blue color on white background.

2. The tent roof design of the Harbour Crest Arena.

We attach our current LWPT presentation, which gives you an idea of who we are, what our business is and what distinguishes us.

The new website design should express that we provide very reliable, high-quality Intellectual Property services, including patent and trademark services worldwide.

On the one hand, it should professional, on the other it should look young.

The managing partners of our patent law firm are in their 30ies and their 40ies, which is comparably young for a patent law firm of our size. Our team comprises about 20 patent attorneys and altogether 45 people.

Websites of competitors that we like are as follows.

http://www.rml.example
http://dorsellquaint.example
http://www.pellard.example
http://www.vrmlaw.example (here we like the structure, rather than the design)

There are two features that all these websites have in common and that we also would like to have implemented in our new website design.

1. A clear and self-explaining main menu in the header.

For example:

HOME OUR FIRM WHAT WE DO WHO WE ARE OUR CLIENTS OUR FEES CONTACT US

2. At least on the main page: A background picture filling the entire screen and having an appealing graphic. Maybe the tent roof of the Harbour Crest Arena?

Further points that we believe to be important are as follows:

1. Our new website should have a simple menu navigation (not as complicated as the current one). It should have two levels, namely the main page and the subpages, that are all directly accessible via the main page, so that all the content can be reached with two clicks.

2. On the WHO WE ARE subpage we like the solution that there is a list of the names of the patent attorneys in the left column, and upon clicking on a name the full profile of the patent attorney including a photograph of the partner will appear. We will have new photographs of our team prepared and supplied to you.

3. On the WHAT WE DO subpage we like the solution that there is a list of the headlines of our fields of activity, like PATENTS, and upon clicking on a headline a more detailed description of the respective field of activity will appear.

4. Our new website should contain less content than our current website. The text will be supplied by us.

5. What is also very important is that the design will be optimized for access by PCs, by tablets and by smart phones (responsive design).

6. We will need both English and German language versions of the website, including all the subpages. We will provide you with the updated text for all the pages.

Thanks very much in advance for your work and your suggestion.

Best regards,

Jonas Retterby (Partner)

Target Market(s)

Innovative and Patenting Firms worldwide, Innovators, Inventors, Potential new Employees

Industry/Entity Type

Lawyer

Number of Pages Required

5+ page

Font styles to use
Sans Serif

Colors
0555a3
0293ce

Requirements
Must have
• New appealing and modern website, self-explaining and easy menu structure
Nice to have
• Maybe some appealing design showing that we are constantly at the edge of the new technical development
Should not have
• May not look old-fashioned, no complicated menu

```html
<!DOCTYPE html>
<html lang="en">
<head>
<meta charset="utf-8">
<title>LWPT Patentanwälte</title>
<link rel="stylesheet" href="https://fonts.googleapis.com/css2?family=Raleway:wght@400;500;600;800&family=Open+Sans:wght@400;600;700&display=swap">
<style>
:root{
  --brand:#0555a3;
  --brand-light:#0293ce;
  --team-band:#0a8dcc;
  --ink:#222;
  --muted:#777;
  --logo:#7ea6d8;
  --footer:#6d6d6d;
  --white:#fff;
  --park:#5e8a3a;
  --park-dark:#3f5f2a;
  --lake:#3d5a52;
  --roof:#c9ccce;
  --town:#a59c86;
}
*{margin:0;padding:0;box-sizing:border-box}
html,body{width:1200px;height:2203px;overflow:hidden}
body{position:relative;background:var(--white);font-family:"Open Sans",sans-serif;color:var(--ink)}
.abs{position:absolute}

/* header */
.site-header{position:absolute;left:0;top:0;width:1200px;height:109px;background:var(--white)}
.logo{position:absolute;left:0;width:1200px;top:18px;text-align:center;font-family:"Raleway",sans-serif;font-weight:400;font-size:54px;letter-spacing:8px;color:var(--logo)}
.lang{position:absolute;top:70px;display:flex;gap:8px;left:940px}
.lang svg{display:block}

.main-nav{position:absolute;left:0;top:109px;width:1200px;height:50px;background:var(--brand)}
.main-nav a{position:absolute;top:0;height:50px;line-height:50px;color:var(--white);text-decoration:none;font-family:"Raleway",sans-serif;font-weight:500;font-size:14px;letter-spacing:.2px}
.main-nav a.active{background:var(--brand-light);width:123px;text-align:center;left:182px}

/* hero */
.hero{position:absolute;left:0;top:159px;width:1200px;height:500px;overflow:hidden}
.hero-photo{position:absolute;inset:0;
  background:
    radial-gradient(ellipse 260px 150px at 560px 300px,rgba(46,74,66,.95) 0%,rgba(46,74,66,0) 100%),
    radial-gradient(ellipse 420px 260px at 1000px 250px,rgba(214,214,210,.85) 0%,rgba(214,214,210,0) 100%),
    radial-gradient(ellipse 330px 200px at 860px 470px,rgba(196,198,198,.9) 0%,rgba(196,198,198,0) 100%),
    radial-gradient(ellipse 420px 260px at 200px 300px,rgba(108,150,60,.95) 0%,rgba(108,150,60,0) 100%),
    linear-gradient(180deg,#9a947f 0%,#7f8a66 18%,var(--park) 40%,var(--park-dark) 70%,#6d7568 100%);}
.hero-shade{position:absolute;inset:0;background:rgba(0,0,0,.12)}
.hero-title{position:absolute;top:152px;left:0;width:1200px;text-align:center;color:var(--white);font-family:"Raleway",sans-serif;font-weight:800;font-size:46px;letter-spacing:.5px}
.hero-sub{position:absolute;top:211px;left:0;width:1200px;text-align:center;color:var(--white);font-family:"Raleway",sans-serif;font-weight:500;font-size:28px;letter-spacing:.5px}
.hero-btn{position:absolute;left:535px;top:269px;width:130px;height:34px;border:2px solid var(--white);color:var(--white);font-size:12px;font-weight:600;line-height:30px;text-align:center;letter-spacing:.5px}
.hero-arrow{position:absolute;top:180px}

/* features */
.features{position:absolute;left:0;top:617px;width:1200px;height:342px;
  background:
    radial-gradient(ellipse 300px 200px at 160px 250px,rgba(190,195,190,.6) 0%,rgba(190,195,190,0) 100%),
    radial-gradient(ellipse 300px 220px at 1080px 260px,rgba(195,198,200,.6) 0%,rgba(195,198,200,0) 100%),
    linear-gradient(180deg,#f4f4f4 0%,#e6e6e6 100%)}
.feature{position:absolute;top:71px;width:260px;text-align:center}
.feature-icon{width:96px;height:96px;border-radius:50%;background:var(--brand);margin:0 auto;display:flex;align-items:center;justify-content:center}
.feature h3{margin-top:22px;font-family:"Raleway",sans-serif;font-weight:500;font-size:18px;color:#222;letter-spacing:.3px}
.feature p{margin:6px auto 0;width:240px;font-size:10px;line-height:18px;color:#777}
.btn-outline{display:inline-block;margin-top:22px;width:101px;height:29px;line-height:25px;border:2px solid var(--brand-light);background:var(--white);color:var(--brand);font-size:9px;font-weight:600;letter-spacing:.3px}

/* welcome */
.welcome-title{position:absolute;left:194px;top:1030px;font-family:"Raleway",sans-serif;font-weight:400;font-size:29px;color:#111;letter-spacing:.3px}
.welcome-rule{position:absolute;left:194px;top:1074px;width:88px;height:2px;background:#111}
.welcome-lead{position:absolute;left:200px;top:1090px;width:470px;font-size:14px;line-height:20px;color:#333}
.welcome-body{position:absolute;left:200px;top:1143px;width:480px;font-size:12px;line-height:20px;color:#888}
.welcome-photo{position:absolute;left:693px;top:1012px;width:325px;height:226px;
  background:
    radial-gradient(ellipse 90px 130px at 70px 120px,rgba(40,36,32,.9) 0%,rgba(40,36,32,0) 100%),
    radial-gradient(ellipse 140px 110px at 250px 90px,rgba(226,206,160,.9) 0%,rgba(226,206,160,0) 100%),
    linear-gradient(90deg,#3f362e 0%,#7c6a52 40%,#b9a47c 75%,#d6c6a0 100%)}

/* team */
.team{position:absolute;left:0;top:1318px;width:1200px;height:362px;background:var(--team-band)}
.team h2{position:absolute;top:32px;left:0;width:1200px;text-align:center;color:var(--white);font-family:"Raleway",sans-serif;font-weight:500;font-size:23px;letter-spacing:.5px}
.member{position:absolute;top:85px;width:200px;text-align:center;color:var(--white)}
.member-photo{width:140px;height:140px;border-radius:50%;margin:0 auto;border:3px solid var(--white);
  background:
    radial-gradient(ellipse 40px 50px at 50% 42%,rgba(200,200,200,.9) 0%,rgba(200,200,200,0) 100%),
    linear-gradient(180deg,#f2f2f2 0%,#cfcfcf 55%,#3a3a3a 78%,#222 100%)}
.member h4{margin-top:8px;font-family:"Raleway",sans-serif;font-weight:500;font-size:14px}
.member p{font-size:10px;line-height:16px;margin-top:2px;opacity:.95}
.member a{display:block;margin-top:3px;font-size:10px;font-weight:700;color:var(--white);text-decoration:none}
.team-divider{position:absolute;top:89px;width:1px;height:221px;background:rgba(255,255,255,.35)}

/* news */
.news-title{position:absolute;left:182px;top:1724px;font-family:"Raleway",sans-serif;font-weight:400;font-size:28px;color:#333}
.see-all{position:absolute;left:959px;top:1742px;width:80px;height:22px;line-height:22px;text-align:center;background:var(--brand);color:var(--white);font-size:11px}
.post{position:absolute;top:1780px;width:256px}
.post-photo{width:256px;height:122px}
.post h4{margin-top:20px;font-size:15px;font-weight:400;color:#222}
.post p{margin-top:6px;font-size:10px;line-height:17px;color:#777}
.post a{display:block;margin-top:7px;font-size:11px;font-weight:700;color:var(--brand);text-decoration:none}

/* footer */
.site-footer{position:absolute;left:0;top:2070px;width:1200px;height:133px;background:var(--footer);color:var(--white)}
.footer-nav{position:absolute;left:181px;top:32px;display:flex;gap:24px}
.footer-nav a{color:var(--white);text-decoration:none;font-size:11px;font-weight:600}
.copyright{position:absolute;left:181px;top:56px;font-size:10px;color:#b5b5b5}
.social{position:absolute;left:183px;top:83px;display:flex;gap:6px}
.social span{width:28px;height:28px;border-radius:50%;background:var(--white)}
.address{position:absolute;right:182px;top:27px;text-align:right;font-size:10px;line-height:17px;color:var(--white);font-style:normal}
</style>
</head>
<body>

<header class="site-header">
  <div class="logo">lwpt</div>
  <div class="lang">
    <svg width="33" height="20" viewBox="0 0 33 20" aria-label="Deutsch"><rect width="33" height="7" fill="#000"/><rect y="7" width="33" height="6" fill="#dd0000"/><rect y="13" width="33" height="7" fill="#ffce00"/></svg>
    <svg width="33" height="20" viewBox="0 0 33 20" aria-label="English"><rect width="33" height="20" fill="#012169"/><path d="M0 0L33 20M33 0L0 20" stroke="#fff" stroke-width="4"/><path d="M0 0L33 20M33 0L0 20" stroke="#c8102e" stroke-width="1.5"/><path d="M16.5 0V20M0 10H33" stroke="#fff" stroke-width="6"/><path d="M16.5 0V20M0 10H33" stroke="#c8102e" stroke-width="3.5"/></svg>
  </div>
</header>

<nav class="main-nav">
  <a class="active" href="#">HOME</a>
  <a href="#" style="left:358px">OUR FIRM</a>
  <a href="#" style="left:517px">WHAT WE DO</a>
  <a href="#" style="left:701px">OUR PEOPLE</a>
  <a href="#" style="left:880px">CONTACT US</a>
</nav>

<section class="hero">
  <div class="hero-photo" role="img" aria-label="Aerial view of the Harbour Crest Arena tent roof beside a park and lake"></div>
  <div class="hero-shade"></div>
  <svg class="hero-arrow" style="left:137px" width="20" height="36" viewBox="0 0 20 36"><path d="M17 3L4 18l13 15" fill="none" stroke="#fff" stroke-width="4"/></svg>
  <svg class="hero-arrow" style="left:1060px" width="20" height="36" viewBox="0 0 20 36"><path d="M3 3l13 15L3 33" fill="none" stroke="#fff" stroke-width="4"/></svg>
  <h1 class="hero-title">LEGAL SERVICE &amp; EXPERTISE</h1>
  <div class="hero-sub">MAECENAS ALIQUET VELIT TURPIS</div>
  <div class="hero-btn">LEARN MORE</div>
</section>

<section class="features" role="img" aria-label="Faded aerial city view background">
  <div class="feature" style="left:200px">
    <div class="feature-icon">
      <svg width="44" height="50" viewBox="0 0 44 50"><rect x="6" y="3" width="32" height="44" fill="none" stroke="#fff" stroke-width="2.5"/><rect x="11" y="9" width="8" height="8" fill="none" stroke="#fff" stroke-width="2"/><path d="M22 11h11M22 15h11M11 22h22M11 27h22M11 32h22M11 37h16" stroke="#fff" stroke-width="2"/></svg>
    </div>
    <h3>WHAT WE DO</h3>
    <p>Praesent elementum elit at tellus Curabitur metus ipsum luctus eu malesuadFusce tellus Sed metus augue convallis et vehicula ut pulvina</p>
    <span class="btn-outline">LEARN MORE</span>
  </div>
  <div class="feature" style="left:477px">
    <div class="feature-icon">
      <svg width="56" height="44" viewBox="0 0 56 44" fill="#fff"><circle cx="12" cy="10" r="5"/><circle cx="28" cy="8" r="6"/><circle cx="44" cy="10" r="5"/><rect x="5" y="17" width="14" height="20" rx="4"/><rect x="20" y="16" width="16" height="24" rx="4"/><rect x="37" y="17" width="14" height="20" rx="4"/></svg>
    </div>
    <h3>OUR PEOPLE</h3>
    <p>Praesent elementum elit at tellus Curabitur metus ipsum luctus eu malesuadFusce tellus Sed metus augue convallis</p>
    <span class="btn-outline">LEARN MORE</span>
  </div>
  <div class="feature" style="left:763px">
    <div class="feature-icon">
      <svg width="56" height="50" viewBox="0 0 56 50" fill="none" stroke="#fff" stroke-width="2"><path d="M28 4v40M8 10h40M18 46h20"/><path d="M8 10L2 26M8 10l6 16M48 10l-6 16M48 10l6 16"/><path d="M2 26q6 6 12 0Z M42 26q6 6 12 0Z" fill="#fff"/></svg>
    </div>
    <h3>OUR FIRM</h3>
    <p>Praesent elementum elit at tellus Curabitur metus ipsum luctus eu malesuadFusce tellus Sed metus augue convallis et</p>
    <span class="btn-outline">LEARN MORE</span>
  </div>
</section>

<svg class="abs" style="left:0;top:600px" width="1200" height="60" viewBox="0 0 1200 60" aria-hidden="true"><path d="M0 17 Q600 -15 1200 17 L1200 60 L0 60Z" fill="#f4f4f4"/></svg>

<section>
  <h2 class="welcome-title">WELCOME TO LWPT</h2>
  <div class="welcome-rule"></div>
  <p class="welcome-lead">apibus malesuada fringilla eu condimentum quis tellus Aenean porttitor eros vel dolor Donec convallis pede venenatis nibh Duis quam</p>
  <p class="welcome-body">Mauris vel lacus vitae felis vestibulum volutpat imperdiet ac nisl Cum sociis natoque penatibus et magnis dis parturient montes nascetur ridiculus mus In iaculis facilisis massa Etiam eu urna Sed porta Suspendisse quam leo molestie sed luctus quis feugiat in pede Fusce tellus Sed metus augue convallis et vehicula</p>
  <div class="welcome-photo" role="img" aria-label="Statue of Justice holding scales in a warm-lit law library"></div>
</section>

<section class="team">
  <h2>OUR TEAM</h2>
  <div class="member" style="left:200px">
    <div class="member-photo" role="img" aria-label="Portrait photo of Jonas C. Retterby"></div>
    <h4>Jonas C. Retterby</h4>
    <p>Praesent elementum elit at tellus<br>Curabitur metus ipsum</p>
    <a href="#">READ MORE</a>
  </div>
  <div class="team-divider" style="left:400px"></div>
  <div class="member" style="left:404px">
    <div class="member-photo" role="img" aria-label="Portrait photo of Malte Brandorf-Keil"></div>
    <h4>Malte Brandorf-Keil</h4>
    <p>Praesent elementum elit at tellus<br>Curabitur metus ipsum</p>
    <a href="#">READ MORE</a>
  </div>
  <div class="team-divider" style="left:602px"></div>
  <div class="member" style="left:604px">
    <div class="member-photo" role="img" aria-label="Portrait photo of Ulrich-Ben Sandholt"></div>
    <h4>Ulrich-Ben Sandholt</h4>
    <p>Praesent elementum elit at tellus<br>Curabitur metus ipsum</p>
    <a href="#">READ MORE</a>
  </div>
  <div class="team-divider" style="left:804px"></div>
  <div class="member" style="left:808px">
    <div class="member-photo" role="img" aria-label="Portrait photo of Dominik A. Verrath"></div>
    <h4>Dominik A. Verrath</h4>
    <p>Praesent elementum elit at tellus<br>Curabitur metus ipsum</p>
    <a href="#">READ MORE</a>
  </div>
</section>

<section>
  <h2 class="news-title">News &amp; Blogs</h2>
  <div class="see-all">See All</div>
  <article class="post" style="left:185px">
    <div class="post-photo" role="img" aria-label="Classical white columns of a courthouse" style="background:linear-gradient(90deg,#8e8e8e 0%,#e6e6e6 18%,#9a9a9a 30%,#e2e2e2 55%,#a0a0a0 70%,#e4e4e4 88%,#9c9c9c 100%)"></div>
    <h4>Fusce tellus Sed metus augue</h4>
    <p>convallis et vehicula ut pulvinar eu ante Integer orci tellus tristique vitae consequat nec</p>
    <a href="#">READ MORE</a>
  </article>
  <article class="post" style="left:482px">
    <div class="post-photo" role="img" aria-label="Business team meeting at a conference table by a window" style="background:radial-gradient(ellipse 120px 50px at 50% 85%,rgba(40,40,46,.9) 0%,rgba(40,40,46,0) 100%),linear-gradient(180deg,#b8c8d4 0%,#7d8fa0 40%,#3e444c 75%,#2a2c31 100%)"></div>
    <h4>Donec convallis pede venenatis</h4>
    <p>convallis et vehicula ut pulvinar eu ante Integer orci tellus tristique vitae consequat nec</p>
    <a href="#">READ MORE</a>
  </article>
  <article class="post" style="left:783px">
    <div class="post-photo" role="img" aria-label="Colleagues reviewing documents around a wooden desk" style="background:radial-gradient(ellipse 110px 45px at 50% 65%,rgba(240,236,228,.95) 0%,rgba(240,236,228,0) 100%),linear-gradient(180deg,#a8b8ca 0%,#8ea2ba 30%,#c49a72 60%,#d9b48e 100%)"></div>
    <h4>Aliquam erat volutpat</h4>
    <p>convallis et vehicula ut pulvinar eu ante Integer orci tellus tristique vitae consequat nec</p>
    <a href="#">READ MORE</a>
  </article>
</section>

<footer class="site-footer">
  <nav class="footer-nav">
    <a href="#">HOME</a><a href="#">OUR FIRM</a><a href="#">WHAT WE DO</a><a href="#">OUR PEOPLE</a><a href="#">CONTACT US</a>
  </nav>
  <div class="copyright">© 2016 Company Name &nbsp;All right reserved &nbsp;Term of Use</div>
  <div class="social" aria-label="Social links"><span></span><span></span><span></span></div>
  <address class="address">
    LWPT Patentanwälte<br>
    Lindqvar . Weiss - Paltrow . Thorne<br>
    Kastellweg 12<br>
    D-80001 Musterstadt
  </address>
</footer>

</body>
</html>
```